wardrobe/costume stylist needs good business card for own business

Hi:)

I'm wanting a business card for my company. I am a freelance stylist.

I do wardrobe/costume stylist to TV commercials; Films; Fashion and Lifestyle shoots.

I'd like a design based around my name Rosalind Pember written nicely, maybe a colour? Up to you?!

I've attached a couple of images of business cards I like
.... be creative and have fun!

Thank you :)
Updates

Reason: I was trying to get my new business card ready for before I headed overseas Friday morning but I don't think that was realistic so I'd like to extend the deadline to give time to the project. Thank you

Hi designers:) Thank you for all your designs, I've extended the deadline until Sunday, so there's a bit more time. I've attached 3 pictures of business cards which I quite like, please take a look to see if it can be of help in your process. I like the pale plain or patterned background with dark font and the dark plain or patterned background with the pale font the motifs the feminine fonts the plain fonts I like the idea of playing with a circle or some shape on one side of the card with my name or initials as in the picture I have on my post could you play around with this idea a bit please? Thank you all for the work you've done :) Rosa

Hi I am working overseas til Saturday night sorry for no feedback until I teturn Thanks :) Rosa

Hi designers, Thank you all so much for submitting your designs, I really appreciate your input into my project :) I'm sorry I didn't get to respond to some comments, and give feedback. I didn't back from being away until later than I expected, and the deadline had passed then, so apologies. Thanks to you all again for all your really good designs :) Rosa

Target Market(s)

I am a freelance stylist my target audience is producers, production companies, photographers, directors...

Industry/Entity Type

Business

Requirements
Must have
• Rosalind Pember
Stylist or Wardrobe Stylist

email rosapember@quillnet.co.nz
Mobile 0218846193

(Don't have to use the words 'email' and 'mobile')
Nice to have
• Would like it to be double sided
Like B & W
Like pale colour background with dark font or white font
Like dark colour background with pale font
Should not have
• I would prefer it not to incorporate pictures

```html
<!DOCTYPE html>
<html lang="en">
<head>
<meta charset="utf-8">
<title>Rosalind Pember – Wardrobe Stylist Business Card</title>
<link rel="stylesheet" href="https://fonts.googleapis.com/css2?family=Yellowtail&family=Roboto+Condensed:wght@400;700&display=swap">
<style>
  :root {
    --page: #e6e7e9;
    --blue-light: #2b8fe0;
    --blue: #1565c0;
    --blue-deep: #0b3f86;
    --ink: #050608;
    --ink-soft: #1a1c20;
    --white: #ffffff;
    --name-blue-a: #2a6fd6;
    --name-blue-b: #123f8f;
  }
  * { box-sizing: border-box; margin: 0; padding: 0; }
  html, body {
    width: 1200px; height: 480px; overflow: hidden;
    background: var(--page);
  }
  .canvas {
    position: relative; width: 1200px; height: 480px;
    display: flex; align-items: center; justify-content: center; gap: 40px;
  }
  .card {
    position: relative; width: 540px; height: 300px; overflow: hidden;
    box-shadow: 0 6px 18px rgba(0,0,0,.25);
    background: var(--ink);
  }
  .card-bg { position: absolute; inset: 0; width: 100%; height: 100%; }

  .brand {
    position: absolute; display: flex; align-items: center; gap: 8px;
    font-family: "Roboto Condensed", sans-serif; font-weight: 700;
    font-size: 17px; letter-spacing: .06em; color: var(--white);
    text-transform: uppercase;
  }
  .brand-dot {
    width: 30px; height: 30px; border-radius: 50%;
    background: var(--ink-soft); border: 3px solid var(--white);
  }
  .front .brand { left: 40px; top: 34px; }
  .back .brand { left: 50%; top: 47%; transform: translate(-50%, -50%); font-size: 22px; }
  .back .brand-dot { width: 40px; height: 40px; }

  .contact {
    position: absolute; left: 318px; top: 30px;
    font-family: "Roboto Condensed", sans-serif; font-size: 14px; color: var(--white);
    list-style: none;
  }
  .contact li { display: flex; align-items: center; gap: 8px; height: 24px; }
  .contact svg { width: 14px; height: 14px; flex: none; }

  .identity { position: absolute; left: 38px; top: 118px; color: var(--white); z-index: 2; }
  .identity-name {
    font-family: "Yellowtail", cursive; font-size: 36px; line-height: 1.05;
    white-space: nowrap;
  }
  .identity-role {
    font-family: "Roboto Condensed", sans-serif; font-size: 14px;
    letter-spacing: .04em; text-transform: uppercase; margin-top: 2px;
  }

  .name-display { position: absolute; inset: 0; width: 100%; height: 100%; z-index: 1; }
  .name-display text {
    font-family: "Yellowtail", cursive; font-size: 84px;
  }
</style>
</head>
<body>
<main class="canvas">

  <section class="card front" aria-label="Card front">
    <svg class="card-bg" viewBox="0 0 540 300" preserveAspectRatio="none" aria-hidden="true">
      <defs>
        <linearGradient id="frontBlue" x1="0" y1="0" x2="1" y2="1">
          <stop offset="0" stop-color="var(--blue-light)"/>
          <stop offset=".6" stop-color="var(--blue)"/>
          <stop offset="1" stop-color="var(--blue-deep)"/>
        </linearGradient>
        <linearGradient id="frontInk" x1="0" y1="0" x2="0" y2="1">
          <stop offset="0" stop-color="var(--ink-soft)"/>
          <stop offset="1" stop-color="var(--ink)"/>
        </linearGradient>
      </defs>
      <rect width="540" height="300" fill="url(#frontInk)"/>
      <polygon points="0,0 540,0 540,100 0,215" fill="url(#frontBlue)"/>
    </svg>

    <svg class="name-display" viewBox="0 0 540 300" aria-hidden="true">
      <defs>
        <linearGradient id="nameBlue" x1="0" y1="0" x2="0" y2="1">
          <stop offset="0" stop-color="var(--name-blue-a)"/>
          <stop offset="1" stop-color="var(--name-blue-b)"/>
        </linearGradient>
      </defs>
      <text x="14" y="280" transform="rotate(-8 14 280)" textLength="506" lengthAdjust="spacingAndGlyphs" fill="url(#nameBlue)">RosalindPember</text>
    </svg>

    <div class="brand"><span class="brand-dot"></span>Pember</div>

    <ul class="contact">
      <li>
        <svg viewBox="0 0 14 14" aria-hidden="true"><rect x="3.5" y="0.5" width="7" height="13" rx="1.5" fill="none" stroke="var(--white)"/><line x1="6" y1="11.5" x2="8" y2="11.5" stroke="var(--white)"/></svg>
        0218846193
      </li>
      <li>
        <svg viewBox="0 0 14 14" aria-hidden="true"><rect x="0.5" y="3" width="13" height="9" fill="var(--white)"/><polyline points="0.5,3 7,8 13.5,3" fill="none" stroke="var(--ink)"/></svg>
        rosapember@quillnet.co.nz
      </li>
    </ul>

    <div class="identity">
      <p class="identity-name">Rosalind Pember</p>
      <p class="identity-role">Wardrobe Stylist</p>
    </div>
  </section>

  <section class="card back" aria-label="Card back">
    <svg class="card-bg" viewBox="0 0 540 300" preserveAspectRatio="none" aria-hidden="true">
      <defs>
        <linearGradient id="backBlue" x1="0" y1="0" x2="1" y2="1">
          <stop offset="0" stop-color="var(--blue-deep)"/>
          <stop offset=".45" stop-color="var(--blue)"/>
          <stop offset="1" stop-color="var(--blue-light)"/>
        </linearGradient>
        <linearGradient id="backInk" x1="0" y1="0" x2="0" y2="1">
          <stop offset="0" stop-color="var(--ink-soft)"/>
          <stop offset="1" stop-color="var(--ink)"/>
        </linearGradient>
      </defs>
      <rect width="540" height="300" fill="url(#backInk)"/>
      <polygon points="0,0 540,0 540,80 0,168" fill="url(#backBlue)"/>
    </svg>

    <div class="brand"><span class="brand-dot"></span>Pember</div>
  </section>

</main>
</body>
</html>
```